Plakat für Hersteller von maßgefertigten Tischunikaten aus Massivholz
Zielgruppe
Wir sind einen Firma die sich auf die Fertigung von maßgefertigten Tischunikaten aus Massivholz spezialisiert hat. Unsere Zielgruppe sind Design affine Leute, im Alter von 35-55 Jahren
Aufgabenstellung
Wir benötigen das Design für eine Messewand mit den Maßen 443X227 cm. 5 Zentimeter rundlaufen dürfen keine Elemente mehr platziert werden. Die Messewand steht im Hintergrund von unserem Stand bei verschiedenen Designmessen
Infos die auf die Messewand müssen: Logo, Tischmanufaktur aus Stuttgart, Maßgefertigte Tischunikate (Bei der Formulierung bin ich flexibel, ihr könnt bspw. auch nur Stichworte benutzen, aber Stuttgart und maßgefertigt ist wichtig).
Die Messewand soll sehr minimalistisch gestaltet sein, bei der letzten Messewand hatten wir ein Foto von einem Tisch im Hintergrund und das sah merkwürdig aus.

```html
<!DOCTYPE html>
<html lang="de">
<head>
<meta charset="utf-8">
<title>Birkenfeld Manufaktur – Messewand</title>
<link rel="stylesheet" href="https://fonts.googleapis.com/css2?family=Montserrat:wght@700&family=Roboto+Slab:wght@500&display=swap">
<style>
  :root {
    --page-bg: #e6e6e6;
    --wall-light: #3d3d3d;
    --wall-mid: #2c2c2c;
    --wall-dark: #202020;
    --ink: #ffffff;
    --accent: #507a3c;
  }
  * { margin: 0; padding: 0; box-sizing: border-box; }
  html, body {
    width: 1200px;
    height: 816px;
    overflow: hidden;
    background: var(--page-bg);
  }
  .trade-wall {
    position: absolute;
    left: 0;
    top: 100px;
    width: 1200px;
    height: 615px;
    overflow: hidden;
    color: var(--ink);
    font-family: "Montserrat", Arial, sans-serif;
  }
  .contour-backdrop {
    position: absolute;
    inset: 0;
    background: radial-gradient(ellipse at 0% 0%, #545454 0%, var(--wall-light) 18%, var(--wall-mid) 50%, var(--wall-dark) 100%);
  }
  .brand {
    position: absolute;
    top: 42px;
    left: 0;
    width: 100%;
    display: flex;
    justify-content: center;
    align-items: center;
    gap: 12px;
  }
  .brand-dot {
    width: 78px;
    height: 78px;
    border: 3px solid var(--ink);
    border-radius: 50%;
    flex: none;
  }
  .brand-name {
    font-family: "Roboto Slab", Georgia, serif;
    font-weight: 500;
    font-size: 29px;
    line-height: 33px;
    color: var(--ink);
  }
  .headline-line {
    position: absolute;
    left: 0;
    width: 100%;
    text-align: center;
    font-weight: 700;
    font-size: 84px;
    line-height: 1;
    letter-spacing: 1px;
  }
  .headline-line.first { top: 150px; }
  .headline-line.second { top: 241px; }
  .location {
    position: absolute;
    top: 344px;
    left: 0;
    width: 100%;
    display: flex;
    justify-content: center;
    align-items: center;
    gap: 14px;
    font-weight: 700;
    font-size: 40px;
    letter-spacing: 0.5px;
  }
  .location-city {
    display: inline-block;
    background: var(--accent);
    border-radius: 10px;
    height: 55px;
    line-height: 55px;
    padding: 0 21px;
  }
  .website {
    position: absolute;
    top: 558px;
    left: 0;
    width: 100%;
    text-align: center;
    font-weight: 700;
    font-size: 16px;
    letter-spacing: 0.6px;
  }
</style>
</head>
<body>
  <section class="trade-wall">
    <div class="contour-backdrop" role="img" aria-label="Dunkler Hintergrund mit feinen grauen Höhenlinien wie Holzmaserung"></div>
    <div class="brand">
      <span class="brand-dot"></span>
      <span class="brand-name">Birkenfeld<br>Manufaktur</span>
    </div>
    <h1 class="headline-line first">MASSGEFERTIGTE</h1>
    <p class="headline-line second">TISCHUNIKATE</p>
    <p class="location">
      <span class="location-label">HERSTELLUNG IN</span>
      <span class="location-city">STUTTGART</span>
    </p>
    <p class="website">WWW.BIRKENFELD-MANUFAKTUR.DE</p>
  </section>
</body>
</html>
```